Business card Zottelgarten

Business card is for a self-employed dog trainer with own dog school. Name and logo of the dog school are available. Color specifications as well. The design should be classy and minimalist, but also modern. An already existing idea would be: Front: Only the logo Back: Contact data

Font styles to use
Serif
Sans Serif
Other font styles liked:
• Trajan Pro

Colors
f78f20

Requirements
Must have
• Name: Margit Wendler-Rasch Title: Dipl. Dog Trainer Contain my logo Follow my font and color preferences (see files)

```html
<!DOCTYPE html>
<html lang="de">
<head>
<meta charset="utf-8">
<title>Zottelgarten – Visitenkarte</title>
<link href="https://fonts.googleapis.com/css2?family=Cinzel:wght@400&family=Roboto:wght@300;400&display=swap" rel="stylesheet">
<style>
  :root {
    --stage: #5f5f5f;
    --card: #f78f20;
    --ink: #ffffff;
    --shadow: rgba(0, 0, 0, 0.35);
  }
  * { margin: 0; padding: 0; box-sizing: border-box; }
  html, body { width: 1200px; height: 1000px; overflow: hidden; }
  body {
    position: relative;
    background: var(--stage);
    font-family: "Roboto", Arial, sans-serif;
    color: var(--ink);
  }
  .card {
    position: absolute;
    top: 170px;
    width: 390px;
    height: 685px;
    background: var(--card);
    box-shadow: 0 4px 10px var(--shadow);
  }
  .card--contact { left: 197px; }
  .card--brand { left: 614px; }

  .brand {
    position: absolute;
    left: 0;
    width: 100%;
    text-align: center;
  }
  .brand__circle {
    display: block;
    margin: 0 auto;
  }
  .brand__name {
    font-family: "Cinzel", "Times New Roman", serif;
    font-weight: 400;
    font-size: 31px;
    letter-spacing: 2px;
    line-height: 1;
    margin-top: 40px;
  }
  .brand__url {
    font-family: "Cinzel", "Times New Roman", serif;
    font-size: 9.5px;
    letter-spacing: 5.2px;
    margin-top: 3px;
  }
  .card--contact .brand { top: 39px; }
  .card--brand .brand { top: 195px; }

  .person {
    position: absolute;
    left: 46px;
    top: 390px;
  }
  .person__name {
    font-family: "Cinzel", "Times New Roman", serif;
    font-weight: 400;
    font-size: 29px;
    line-height: 1;
    letter-spacing: 0.3px;
  }
  .person__title {
    font-size: 17px;
    font-weight: 300;
    letter-spacing: 0.6px;
    margin-top: 6px;
  }
  .address {
    position: absolute;
    left: 46px;
    top: 474px;
    font-style: normal;
    font-size: 16.5px;
    font-weight: 300;
    line-height: 23px;
  }
  .contacts {
    position: absolute;
    left: 46px;
    top: 540px;
    list-style: none;
    font-size: 16.5px;
    font-weight: 300;
    line-height: 23.5px;
  }
  .contacts li { display: flex; align-items: center; }
  .contacts svg { width: 12px; height: 12px; margin-right: 14px; flex: none; }
</style>
</head>
<body>
  <section class="card card--contact">
    <div class="brand">
      <svg class="brand__circle" width="180" height="180" viewBox="0 0 180 180" aria-hidden="true">
        <circle cx="90" cy="90" r="86" fill="none" stroke="var(--ink)" stroke-width="3"/>
      </svg>
      <div class="brand__name">Zottelgarten</div>
      <div class="brand__url">www.zottelgarten.ch</div>
    </div>

    <div class="person">
      <h1 class="person__name">Margit Wendler-Rasch</h1>
      <p class="person__title">Dipl. Hundetrainerin</p>
    </div>

    <address class="address">
      Lindenweg 14, Wiesental,<br>
      Kreis WT4 2LM
    </address>

    <ul class="contacts">
      <li>
        <svg viewBox="0 0 12 12" aria-hidden="true"><rect x="2.5" y="0.5" width="7" height="11" rx="1.2" fill="none" stroke="var(--ink)"/><circle cx="6" cy="9.5" r="0.7" fill="var(--ink)"/></svg>
        +41 79 555 0182
      </li>
      <li>
        <svg viewBox="0 0 12 12" aria-hidden="true"><rect x="0.5" y="2" width="11" height="8" fill="none" stroke="var(--ink)"/><path d="M0.5 2 L6 6.5 L11.5 2" fill="none" stroke="var(--ink)"/></svg>
        hallo@zottelgarten.ch
      </li>
      <li>
        <svg viewBox="0 0 12 12" aria-hidden="true"><circle cx="6" cy="6" r="5.5" fill="none" stroke="var(--ink)"/><ellipse cx="6" cy="6" rx="2.3" ry="5.5" fill="none" stroke="var(--ink)"/><path d="M0.5 6 H11.5" stroke="var(--ink)"/></svg>
        www.zottelgarten.ch
      </li>
    </ul>
  </section>

  <section class="card card--brand">
    <div class="brand">
      <svg class="brand__circle" width="180" height="180" viewBox="0 0 180 180" aria-hidden="true">
        <circle cx="90" cy="90" r="86" fill="none" stroke="var(--ink)" stroke-width="3"/>
      </svg>
      <div class="brand__name">Zottelgarten</div>
      <div class="brand__url">www.zottelgarten.ch</div>
    </div>
  </section>
</body>
</html>
```